Plakat-Design für Gemeinschaftspraxis
Briefing
Ausgangssituation
Wir sind eine Gemeinschaftspraxis, die aus Ärzten und Physiotherapeuten besteht. Diese sollen unter einer gemeinsamen Marke präsentiert werden, dem sogenannten „Kelvaro“ (Farbcode Grün und Grau). Zusätzlich werden die Physiotherapeuten noch unter einer Marke zusammengefasst, dem sogenannten „Tesmunda“ (Farbcode Blau und Grün).
Kelvaro und Tesmunda haben jeweils eigene Internetseiten, Flyer und auch Visitenkarten.
Da jedoch beide Marken am selben Standort tätig sind, sollen auf diversen Plakaten (die im Umfeld der Ordination hängen werden) und den Schildern an der Türe auch beide Marken gemeinsam präsentiert werden.
Logos inkl. Farbrichtlinien wurden bereits gestaltet. Als Designvorlage dient ebenso ein allgemeiner Flyer über „Kelvaro“ (s. Anhang).
Im Anhang an das Briefing finden Sie alle relevanten Dateien wie Logos, Farbcodes, Fotos etc., die Sie zur Gestaltung der Werbemittel benötigen. Die grafische Umsetzung, Gliederung etc. überlassen wir Ihnen und freuen uns auf übersichtliche Vorschläge. Es wäre schön, wenn sich die Farbcodes der jeweiligen Marken auch in den Werbemitteln widerspiegeln. Wichtig ist uns, dass die Werbemittel klar und gut strukturiert gestaltet sind und nicht überladen wirken.
Hier finden Sie all mögliche Logo-Dateien, den bestehenden Flyer, die Farbwerte ,...
https://filedrop-example.net/t-Xq4bnLzPae
Farbregeln:
Wenn im Werbemittel nur ein Logo vorkommt, dann ist die Farbregel wie folgt:
Farbcode Kelvaro: Grün und Grau
Farbcode Tesmunda: Blau und Grün
Wenn im Werbemittel beide Logos vorkommen, dann ist die Farbregel wie folgt:
Farbcode Kelvaro: bleibt Grün und Grau
Farbcode Tesmunda: wird geändert in Blau und Grau
Viele der Werbemittel werden bei plakatfix.at produziert. Wenn Sie den jeweiligen Link beim Punkt „Datenaufbereitung“ anklicken, können Sie falls nötig auch direkt Formatvorlagen in diver..
Aufgabenstellung
Dieser Auftrag umfasst die Gestaltung von vier Plakaten in div. Größen mit identem Inhalt.
Bitte gestallten Sie zu Beginn nur die Größe 4000x1500cm
Sobald sich das Design in die richtige Richtung entwickelt, können dann auch die anderen Größen angelegt werden.
--> Bei zufriedenstellender Arbeit stehen eine Reihe von Folgeaufträgen an. (Siehe unten)
Plakate (4 Stück)
1. Plakat
Größe: 4000x1500cm
Info: Hängt zur Bewerbung der Praxis im Außenbereich an diversen Standorten in den umliegenden Orten, auf einer Höhe von ca. 3 Metern und soll vor allem vorbeifahrende Autofahrer ansprechen.
Inhalt:
Die Logos Kelvaro und Tesmunda
Die Adresse: Lindenhofweg 17/3, 2380 Perchtoldsdorf
E-Mailadressen office@kelvaro.net und office@tesmunda.at
Websites: www.kelvaro.net und www.tesmunda.at
Text: „Gemeinschaftspraxis für Orthopädie und Physiotherapie“
Fachbereiche/Schlagwörter: Unfallchirurgie, Sportmedizin, Rehabilitation, Sportphysiotherapie
Weitere optionale Schlagworte: Chiropraktik, Akupunktur, Prävention, Massagen
Datenaufbereitung:
Druckformat: 4060x1560mm
Sicherheitsabstand: 40mm
Abstand vom Ösenmittelpunkt zum Rand: 15mm
Abstand der Ösen zueinander: ca 500mm
Ösendurchmesser: 15mm
https://www.plakatfix.at/produkte/banner-transparente/transparente-planen-banner/
2. Plakat
Größe: 3000x1000mm
Inhalt/Info: identisch zu Plakat Nr. 1 4000x1500, nur das Format ist anders.
Druckformat: 3060x1060mm
3. Plakat
Größe: 4000x850mm
Info: Hängt auf der Fassade unseres Gebäudes und soll den Standort der Ordination klar kennzeichnen. Soll vorbeifahrende Autofahrer und Fußgänger auf die Ordinat..

```html
<!DOCTYPE html>
<html lang="de">
<head>
<meta charset="utf-8">
<title>Kelvaro & Tesmunda – Plakat 3000 x 1000</title>
<link href="https://fonts.googleapis.com/css2?family=Ubuntu:wght@400;500;700&display=swap" rel="stylesheet">
<style>
  :root{
    --green:#76b82a;
    --green-dark:#0f8a3c;
    --blue:#0072c3;
    --grey-text:#666666;
    --label-grey:#6f6f6f;
    --soft-grey:#f1f1f1;
    --frame:#9a9a9a;
    --white:#ffffff;
  }
  *{margin:0;padding:0;box-sizing:border-box}
  html,body{width:1200px;height:1200px;overflow:hidden;background:var(--white);font-family:"Ubuntu",sans-serif}
  .board{position:relative;width:1200px;height:1200px}
  .format-label{position:absolute;top:300px;left:0;width:1200px;text-align:center;font-size:44px;font-weight:400;color:var(--label-grey);letter-spacing:1px}
  .banner{position:absolute;left:94px;top:431px;width:1011px;height:337px;border:1px solid var(--frame);overflow:hidden;background:var(--white)}
  .banner-shapes{position:absolute;left:0;top:0;width:1011px;height:336px}
  .headline{position:absolute;left:35px;top:32px;font-weight:700;font-size:27px;line-height:33px;color:var(--green);letter-spacing:0.3px}
  .headline-rule{position:absolute;left:36px;top:135px;width:306px;height:5px;background:linear-gradient(90deg,var(--green-dark),var(--green))}
  .services{position:absolute;top:148px;list-style:none;font-size:17px;line-height:20.5px;color:var(--grey-text)}
  .services li{position:relative;padding-left:14px}
  .services li::before{content:"";position:absolute;left:0;top:8px;width:5px;height:5px;border-radius:50%;background:var(--green)}
  .services-left{left:36px}
  .services-right{left:227px}
  .brand{position:absolute;display:flex;align-items:center;gap:8px;font-weight:700;font-size:25px}
  .brand-dot{width:40px;height:40px;border-radius:50%}
  .brand-kelvaro{left:36px;top:232px;color:var(--green)}
  .brand-kelvaro .brand-dot{background:var(--green)}
  .brand-tesmunda{left:208px;top:232px;color:var(--blue)}
  .brand-tesmunda .brand-dot{background:var(--blue)}
  .visit-badge{position:absolute;left:416px;top:162px;width:108px;height:108px;border-radius:50%;background:var(--green);color:var(--white);display:flex;align-items:center;justify-content:center;text-align:center;font-weight:700;font-size:14.5px;line-height:18px;letter-spacing:0.3px}
  .web-links{position:absolute;right:35px;top:30px;text-align:right;font-weight:700;font-size:21px;line-height:30px;color:var(--white)}
  .address{position:absolute;right:35px;top:108px;text-align:right;font-size:16.5px;line-height:22px;color:var(--white)}
  .address-pin{position:absolute;left:-24px;top:2px;width:13px;height:19px}
</style>
</head>
<body>
<div class="board">
  <div class="format-label">3000 x 1000</div>

  <div class="banner">
    <svg class="banner-shapes" viewBox="0 0 1011 336" xmlns="http://www.w3.org/2000/svg">
      <defs>
        <clipPath id="photo-area">
          <path d="M517 0 Q440 165 511 336 L1011 336 L1011 0 Z"/>
        </clipPath>
        <linearGradient id="photo-training" x1="0" y1="0" x2="1" y2="1">
          <stop offset="0" stop-color="#eef2f4"/>
          <stop offset="0.6" stop-color="#c9d6df"/>
          <stop offset="1" stop-color="#5f86ad"/>
        </linearGradient>
        <linearGradient id="photo-consult" x1="0" y1="0" x2="1" y2="1">
          <stop offset="0" stop-color="#f1f3f4"/>
          <stop offset="0.55" stop-color="#bfc6cc"/>
          <stop offset="1" stop-color="#b9cf3c"/>
        </linearGradient>
        <linearGradient id="photo-doctor" x1="0" y1="0" x2="1" y2="1">
          <stop offset="0" stop-color="#e9ecee"/>
          <stop offset="0.6" stop-color="#c7c9c9"/>
          <stop offset="1" stop-color="#5aa43a"/>
        </linearGradient>
      </defs>

      <circle class="deco-circle" cx="83" cy="115" r="150" fill="var(--soft-grey)"/>
      <circle class="deco-circle" cx="322" cy="152" r="85" fill="var(--soft-grey)"/>

      <g clip-path="url(#photo-area)">
        <polygon role="img" aria-label="Foto: Physiotherapeut trainiert mit Patient im Therapieraum" fill="url(#photo-training)" points="430,0 780,0 725,90 526,189 430,200"/>
        <polygon role="img" aria-label="Foto: Arzt und Therapeut besprechen Röntgenbild am Behandlungstisch" fill="url(#photo-consult)" points="430,200 526,189 725,90 900,90 837,186 725,336 430,336"/>
        <polygon role="img" aria-label="Foto: Arzt erklärt einem Patienten ein Röntgenbild" fill="url(#photo-doctor)" points="837,186 1011,140 1011,336 725,336"/>
        <line x1="520" y1="192" x2="740" y2="82" stroke="var(--white)" stroke-width="6"/>
        <line x1="722" y1="340" x2="842" y2="180" stroke="var(--white)" stroke-width="6"/>
      </g>

      <path d="M512 0 Q433 165 505 336" fill="none" stroke="var(--green)" stroke-width="9"/>

      <path class="contact-field" d="M702 -5 C728 125 870 225 1016 168 L1016 -5 Z" fill="var(--blue)" stroke="var(--white)" stroke-width="8"/>
    </svg>

    <h1 class="headline">GEMEINSCHAFTSPRAXIS<br>FÜR ORTHOPÄDIE<br>UND PHYSIOTHERAPIE</h1>
    <div class="headline-rule"></div>

    <ul class="services services-left">
      <li>Unfallchirurgie</li>
      <li>Sportmedizin</li>
      <li>Ernährungsberatung</li>
    </ul>
    <ul class="services services-right">
      <li>Rehabilitation</li>
      <li>Sportphysiotherapie</li>
      <li>Massagen</li>
    </ul>

    <div class="brand brand-kelvaro"><span>Kelvaro</span><span class="brand-dot"></span></div>
    <div class="brand brand-tesmunda"><span>Tesmunda</span><span class="brand-dot"></span></div>

    <div class="visit-badge">BESUCHEN<br>SIE UNS!</div>

    <div class="web-links">www.kelvaro.net<br>www.tesmunda.at</div>
    <div class="address">
      <svg class="address-pin" viewBox="0 0 13 19" xmlns="http://www.w3.org/2000/svg">
        <path d="M6.5 0 A6.5 6.5 0 0 1 13 6.5 C13 11 6.5 19 6.5 19 C6.5 19 0 11 0 6.5 A6.5 6.5 0 0 1 6.5 0 Z" fill="var(--green)"/>
        <circle cx="6.5" cy="6.5" r="2.4" fill="var(--blue)"/>
      </svg>
      Lindenhofweg 17/3<br>in Lindenbrunn
    </div>
  </div>
</div>
</body>
</html>
```